Property Investment eBook Cover

I am a long established Australian property investment adviser, analyst and consultant who is now in semi-retired mode and have re-branded to reflect a more casual and personal approach to advising my property investor clients. I am writing a 'revised edition' to a book written in partnership with my father 20 years ago and need an eBook Cover for this new edition. The eBook will be uploaded to all the regular Australian providers (Larkfield Reader, Quince Folio, Tavi, Pagemarten)

The 3 key elements in the book cover are:

Title: The Harvest Engine of Land. The word 'Property' should be larger and more prominent. eg "The Wealth Power of" could be 1/3 the size of "Property" - with both justified left

Edition: Sydney 2021. "Sydney 2021" should be the focus and dominant imagery of the eBook cover and more prominent than the Title or Author

Author: Colin Marsh, The Housing Ledger Guide. The word "Author" should not appear. "The Housing Ledger Guide" should appear underneath Colin Marsh and justified to Colin Marsh, therefore a smaller font.

The cover should be simple, but eye-catching. No property images, more of an abstract background, than a background with an image. Our preferred colour palette is more blues/greens. Prefer SerifFonts

Copy of book published 20 years ago attached for reference only

```html
<!DOCTYPE html>
<html lang="en">
<head>
<meta charset="utf-8">
<title>The Harvest Engine of Land — Sydney 2021</title>
<link rel="stylesheet" href="https://fonts.googleapis.com/css2?family=Cormorant+Garamond:wght@400;500;600&family=Cinzel:wght@400;500&display=swap">
<style>
  :root {
    --paper: #ffffff;
    --ink: #1f1f1f;
    --ink-soft: #3a3a3a;
    --edition-blue: #2b3f9f;
    --leaf-light: #f3f6f3;
    --leaf-mid: #dde6df;
    --leaf-deep: #b9c9bf;
  }
  * { margin: 0; padding: 0; box-sizing: border-box; }
  html, body {
    width: 849px;
    height: 1200px;
    overflow: hidden;
    background: var(--paper);
  }
  .cover {
    position: relative;
    width: 849px;
    height: 1200px;
    background: var(--paper);
    overflow: hidden;
    text-align: center;
  }
  .cover__texture {
    position: absolute;
    left: 0; right: 0; top: 300px; bottom: 0;
    background:
      radial-gradient(ellipse 70% 45% at 20% 70%, var(--leaf-mid) 0%, transparent 70%),
      radial-gradient(ellipse 60% 40% at 85% 45%, var(--leaf-mid) 0%, transparent 70%),
      radial-gradient(ellipse 80% 40% at 55% 100%, var(--leaf-deep) 0%, transparent 75%),
      linear-gradient(180deg, var(--paper) 0%, var(--leaf-light) 25%, var(--leaf-mid) 100%);
  }
  .title {
    position: relative;
    padding-top: 48px;
    font-family: "Cinzel", "Cormorant Garamond", serif;
    color: var(--ink);
  }
  .title__lead {
    display: block;
    font-size: 50px;
    font-weight: 400;
    letter-spacing: 0.32em;
    line-height: 76px;
    padding-left: 0.32em;
  }
  .title__key {
    display: block;
    font-family: "Cormorant Garamond", serif;
    font-size: 112px;
    font-weight: 500;
    letter-spacing: 0.04em;
    line-height: 120px;
    text-transform: uppercase;
  }
  .divider {
    position: relative;
    display: block;
    margin: 22px auto 0;
  }
  .edition {
    position: relative;
    margin-top: 34px;
    font-family: "Cormorant Garamond", serif;
    color: var(--edition-blue);
  }
  .edition__label {
    display: block;
    font-size: 46px;
    font-weight: 500;
    letter-spacing: 0.06em;
    text-transform: uppercase;
    line-height: 60px;
  }
  .edition__place,
  .edition__year {
    display: block;
    font-size: 150px;
    font-weight: 400;
    letter-spacing: 0.04em;
    line-height: 140px;
    text-transform: uppercase;
  }
  .edition__place { margin-top: 36px; }
  .author {
    position: absolute;
    left: 0; right: 0;
    top: 955px;
    font-family: "Cormorant Garamond", serif;
  }
  .author__name {
    display: block;
    font-size: 60px;
    font-weight: 500;
    letter-spacing: 0.06em;
    color: var(--ink);
    text-transform: uppercase;
    line-height: 70px;
  }
  .author__role {
    display: block;
    margin-top: 8px;
    font-size: 30px;
    font-weight: 500;
    letter-spacing: 0.05em;
    color: var(--ink-soft);
    text-transform: uppercase;
  }
</style>
</head>
<body>
  <main class="cover">
    <div class="cover__texture" role="img" aria-label="Abstract pale green and white palm leaf texture"></div>

    <h1 class="title">
      <span class="title__lead">The Harvest</span>
      <span class="title__lead">Engine of</span>
      <span class="title__key">Land</span>
    </h1>

    <svg class="divider" width="420" height="20" viewBox="0 0 420 20" aria-hidden="true">
      <line x1="0" y1="10" x2="420" y2="10" stroke="#1f1f1f" stroke-width="2"/>
      <rect x="203" y="3" width="14" height="14" transform="rotate(45 210 10)" fill="#1f1f1f"/>
    </svg>

    <section class="edition">
      <span class="edition__label">Edition:</span>
      <span class="edition__place">Sydney</span>
      <span class="edition__year">2021</span>
    </section>

    <footer class="author">
      <span class="author__name">Colin Marsh</span>
      <span class="author__role">The Housing Ledger Guide</span>
    </footer>
  </main>
</body>
</html>
```